We need 3 A2 posters similar look but different enough to be eye catching when changed.

We are a healthcare centre that requires 3 A2 posters - simple, similar but different background colours. These posters will be used within our business to promote services we provide to our clients.

The design should include our logo(attached), a large header and a large section in the middle of the poster to promote the event. We need a blank text box (which WE can insert text to advertise), and 1 image to advertise the event. Please note, we do not need you to choose an image we simply would like you to place a demo to give us an idea of where it should sit.

We want to use the bubble design (attached) as a background and the company colours pink, orange and blue - as on our website. Attached is a copy of our logo and background bubble effect. You can also refer to our website - www.marlowpinegroup.com.au for more inspiration.

Just to reiterate, these posters should be simple, different but have a uniform feel. They should have an empty middle section that can be edited to add text and a space for an eye catching title and matching image.

Our services include Chiropractic, Podiatry, Nutrition, Massage, Yoga, Pilates and Specialised rehabilitation classes.

Reason: Hi designers, I know we are all busy but I really need more designs from the designers I invited to this project and look forward to receiving more designs. Any questions please let me know. Regards, Noreen

Reason: Hi all Increased the budget Regards Noreen

Target Market(s)

Corporate Sydney City office workers

Industry/Entity Type

Healthcare

Requirements
Must have
• logo and company colours
section in the middles that can be edited to add text
Space allocated for image placement
Catchy title/header

```html
<!DOCTYPE html>
<html lang="en">
<head>
<meta charset="utf-8">
<title>Nutrition is for you! – Harbour Lane Health</title>
<link href="https://fonts.googleapis.com/css2?family=Tinos:wght@700&family=Arimo:wght@700&family=PT+Sans:wght@400;700&display=swap" rel="stylesheet">
<style>
  :root {
    --pink: #b8337e;
    --pink-soft: #cf5f9c;
    --pink-deep: #a12a6c;
    --orange: #dc8a37;
    --blue: #6263ac;
    --ink: #2a1a22;
    --white: #ffffff;
    --photo-light: #fbf3f7;
    --photo-mid: #d7a1bf;
    --photo-dark: #a8567f;
  }
  * { margin: 0; padding: 0; box-sizing: border-box; }
  html, body { width: 849px; height: 1200px; overflow: hidden; background: var(--white); }
  .poster { position: relative; width: 849px; height: 1200px; overflow: hidden; background: var(--white); }

  .header-bubbles {
    position: absolute; left: 0; top: 0; width: 849px; height: 338px;
    background: linear-gradient(135deg, var(--pink-soft) 0%, var(--pink) 55%, var(--pink-deep) 100%);
  }
  .title-main {
    position: absolute; left: 28px; top: 22px;
    font-family: "Tinos", "Times New Roman", serif; font-weight: 700;
    font-size: 152px; line-height: 1; color: var(--white);
    -webkit-text-stroke: 2px var(--ink);
    text-shadow: 3px 3px 4px rgba(0,0,0,0.35);
    letter-spacing: 1px;
  }
  .title-sub {
    position: absolute; left: 288px; top: 184px;
    font-family: "Arimo", Arial, sans-serif; font-weight: 700;
    font-size: 86px; line-height: 1; color: var(--white);
    letter-spacing: 8px;
    -webkit-text-stroke: 1.5px var(--ink);
    text-shadow: 2px 2px 3px rgba(0,0,0,0.3);
  }
  .rule { position: absolute; right: 0; }
  .rule-blue { background: var(--blue); }
  .rule-orange { background: var(--orange); }
  .rule-pink { background: var(--pink); }

  .feature-image {
    position: absolute; left: 0; top: 338px; width: 849px; height: 830px;
    background:
      linear-gradient(90deg, rgba(168,86,127,0) 82%, rgba(168,86,127,0.45) 90%, rgba(168,86,127,0.2) 100%),
      radial-gradient(ellipse 60% 35% at 45% 8%, var(--photo-light) 0%, rgba(251,243,247,0) 100%),
      radial-gradient(ellipse 45% 40% at 8% 95%, var(--photo-dark) 0%, rgba(168,86,127,0) 100%),
      radial-gradient(ellipse 50% 35% at 85% 92%, #c98aaa 0%, rgba(201,138,170,0) 100%),
      linear-gradient(180deg, #f7e9f0 0%, #e6c2d5 35%, var(--photo-mid) 70%, #c07a9e 100%);
  }
  .promo-copy {
    position: absolute; left: 288px; top: 597px; width: 300px;
    font-family: "PT Sans", "Myriad Pro", sans-serif; font-size: 16px;
    line-height: 21.4px; color: var(--ink);
  }
  .brand-band {
    position: absolute; left: 286px; top: 910px; right: 0; height: 63px;
    background: var(--blue);
    display: flex; align-items: center; padding-left: 16px; gap: 12px;
  }
  .brand-mark { width: 14px; height: 14px; background: var(--white); }
  .brand-name {
    font-family: "PT Sans", sans-serif; font-weight: 700; font-size: 27px;
    color: var(--white);
  }
</style>
</head>
<body>
<main class="poster">
  <div class="header-bubbles" role="img" aria-label="Pink background of soft overlapping rounded-square bubbles"></div>
  <h1 class="title-main">Nutrition</h1>
  <p class="title-sub">is for you!</p>
  <div class="rule rule-blue" style="left:285px; top:307px; height:20px;"></div>
  <div class="rule rule-orange" style="left:285px; top:327px; height:3px;"></div>
  <div class="rule rule-pink" style="left:285px; top:330px; height:8px;"></div>

  <div class="feature-image" role="img" aria-label="Image placeholder: pink-tinted photograph of a breakfast table with a mug, cereal and fresh food"></div>

  <p class="promo-copy">Nutritional Medicine at Harbour Lane Health is scientific and individual. By using a combination of alterations in diet with powerful organic nutrient supple&shy;mentation, we coordinate a realistic plan which suits YOUR health and lifestyle requirements. Working with hundreds of busy corporate workers per week for over 12 years, Harbour Lane Health understands more than any other, the importance of fast, effective programs that achieve real results.</p>

  <div class="brand-band">
    <span class="brand-mark"></span>
    <span class="brand-name">Harbour Lane Health</span>
  </div>

  <div class="rule rule-blue" style="left:0; top:1168px; height:20px;"></div>
  <div class="rule rule-orange" style="left:0; top:1188px; height:3px;"></div>
  <div class="rule rule-pink" style="left:0; top:1191px; height:9px;"></div>
</main>
</body>
</html>
```